Check-up reminder postcard

We require a design for a postcard to remind patients to book their dental check up.

Size: standard postcard 100 x 150mm

We are a small family-focussed dental practice. The design should reflect our brand which is warm & sophisticated as well as incorporate the logo colours. For more information please see our website kellowayfamilydental.com.au.

Target Market(s)

Female aged 30 - 45 years old

Industry/Entity Type

Dental

Requirements
Must have
• The front side should have the copy "We've been missing you...".

Back side of postcard should have area for patient name, address, stamp to be placed. The following copy should be used:

"Dear (please leave space for name)

We've been missing you!

We haven't seen you for your regular dental check up. Please call or visit our website to schedule an appointment. Alternatively, we will be in touch over the next couple of weeks.

We look forward to seeing you again soon!

The Kelloway Family Dental team

Phone: 03 9412 7058 Address: 118 Denholm Road, Kelloway VIC 3152 Web: www.kellowayfamilydental.com.au Email: admin@kellowayfamilydental.com.au"

Include the logo on back side of postcard. Please add the tag line under the logo "Creating beautiful smiles everyday" - sans serif font.

- Design file:
All colours must be converted to CMYK.
Bleed 3mm external from trim.
Trims and registration marks are offset 5mm.
All text to be 3mm from trim if possible.
Nice to have
• Maple leaf as in the logo
Slightly cursive font
Less cluttered look
Should not have
• Cartoons
Pictures of teeth, drills, probes, mirrors
Photos of people

```html
<!DOCTYPE html>
<html lang="en">
<head>
<meta charset="utf-8">
<title>Kelloway Family Dental – Check-up Reminder Postcard</title>
<link href="https://fonts.googleapis.com/css2?family=Cabin:ital,wght@0,400;0,500;1,400&display=swap" rel="stylesheet">
<style>
  :root {
    --teal: #0c8b94;
    --leaf-green: #9bac16;
    --text-grey: #5b5b5d;
    --rule-grey: #b9b9bb;
    --card-white: #ffffff;
    --backdrop: #e9e7e3;
  }
  * { margin: 0; padding: 0; box-sizing: border-box; }
  html, body {
    width: 1200px;
    height: 1161px;
    overflow: hidden;
    background: var(--backdrop);
    font-family: "Cabin", "Gill Sans", sans-serif;
  }
  .canvas { position: relative; width: 1200px; height: 1161px; }
  .postcard {
    position: absolute;
    left: 185px;
    width: 830px;
    height: 553px;
    background: var(--card-white);
    box-shadow: 0 2px 8px rgba(0,0,0,0.12);
  }
  .postcard--front { top: 16px; }
  .postcard--back { top: 590px; }

  /* Brand lockup */
  .brand-mark { border-radius: 50%; background: var(--leaf-green); flex: none; }
  .brand-name { color: var(--teal); font-weight: 400; text-transform: uppercase; line-height: 1; }
  .brand-name .line-main, .brand-name .line-sub { display: block; }

  /* Front */
  .front-brand {
    position: absolute;
    right: 36px;
    top: 150px;
    display: flex;
    align-items: center;
    gap: 26px;
  }
  .front-brand .brand-mark { width: 120px; height: 120px; }
  .front-brand .brand-name { text-align: right; }
  .front-brand .line-main { font-size: 92px; letter-spacing: 1px; }
  .front-brand .line-sub { font-size: 58px; letter-spacing: 3px; margin-top: 10px; }
  .front-tagline {
    position: absolute;
    right: 36px;
    top: 380px;
    font-style: italic;
    font-size: 31px;
    color: var(--leaf-green);
  }

  /* Back */
  .back-brand {
    position: absolute;
    left: 12px;
    top: 12px;
    display: flex;
    align-items: center;
    gap: 10px;
  }
  .back-brand .brand-mark { width: 44px; height: 44px; }
  .back-brand .line-main { font-size: 33px; }
  .back-brand .line-sub { font-size: 24px; letter-spacing: 1px; margin-top: 2px; }
  .smile-tagline {
    position: absolute;
    left: 66px;
    top: 80px;
    font-size: 16px;
    color: var(--leaf-green);
  }
  .message {
    position: absolute;
    left: 25px;
    top: 176px;
    font-size: 19px;
    line-height: 26px;
    color: var(--text-grey);
  }
  .signature {
    position: absolute;
    left: 25px;
    top: 346px;
    font-size: 17px;
    font-style: italic;
    color: var(--text-grey);
  }
  .contact {
    position: absolute;
    left: 25px;
    top: 430px;
    font-size: 17px;
    line-height: 24px;
    color: var(--teal);
  }

  /* Mailing area */
  .stamp-box {
    position: absolute;
    right: 24px;
    top: 24px;
    width: 84px;
    height: 100px;
    border: 1.5px dashed var(--rule-grey);
  }
  .address-lines {
    position: absolute;
    left: 560px;
    right: 24px;
    top: 260px;
    list-style: none;
  }
  .address-lines li {
    height: 46px;
    border-bottom: 1px solid var(--rule-grey);
  }
</style>
</head>
<body>
<div class="canvas">

  <section class="postcard postcard--front">
    <div class="front-brand">
      <span class="brand-mark"></span>
      <div class="brand-name">
        <span class="line-main">Kelloway</span>
        <span class="line-sub">Family Dental</span>
      </div>
    </div>
    <p class="front-tagline">We've been missing you...</p>
  </section>

  <section class="postcard postcard--back">
    <div class="back-brand">
      <span class="brand-mark"></span>
      <div class="brand-name">
        <span class="line-main">Kelloway</span>
        <span class="line-sub">Family Dental</span>
      </div>
    </div>
    <p class="smile-tagline">Creating beautiful smiles everyday</p>

    <div class="message">
      <p>Dear ........................................</p>
      <p>We've been missing you as we haven't seen you</p>
      <p>for your dental check up.</p>
      <p>Over the next couple of weeks we will be in touch otherwise,</p>
      <p>please call or visit our website to book an appointment.</p>
      <p>We look forward to seeing you again soon!</p>
    </div>

    <p class="signature">The Kelloway Family Dental team</p>

    <div class="contact">
      <p>Phone: 03 9412 7058</p>
      <p>Address: 118 Denholm Road, Kelloway VIC 3152</p>
      <p>Web: www.kellowayfamilydental.com.au</p>
      <p>Email: admin@kellowayfamilydental.com.au</p>
    </div>

    <div class="stamp-box" aria-label="Place stamp here"></div>
    <ul class="address-lines" aria-label="Patient name and address">
      <li></li><li></li><li></li><li></li>
    </ul>
  </section>

</div>
</body>
</html>
```